Consulting company needs website design

We need a simple, static website design for our consulting company. We are looking for a general design of the look and feel of the website. Initially, it will have these pages:
- Home
- About us
- Services
- Contact us
We have our own logo which I have attached to the brief.

We are looking for a simple website, with white background and the use of gray (darker) as the main theme. Simple fonts. The website should be responsive so it an be easily red in mobile devices.

As part of the project, we will need to receive at least the following items:
- Individual files with sample text to support the pages outlined above
- Necessary CSS files

Our current website is here: http://www.lantrovale.co/

Here are some examples of other website we like to be used as guideline:
- http://www.morvicaplanos.com/
-

Target Market(s)

Individuals and companies looking to hire our company to provide consulting services.

Industry/Entity Type

It Company

Coding

Coded - Design and coding required

Number of Pages Required

4 page

Font styles to use
Sans Serif

Requirements
Must have
• Main page should have the ability to embed Chirplet feed into it.
• We prefer the design to use gray tones.

```html
<!DOCTYPE html>
<html lang="en">
<head>
<meta charset="utf-8">
<title>Lantrovale Group – Consulting Company</title>
<link rel="stylesheet" href="https://fonts.googleapis.com/css2?family=Roboto:wght@300;400;500;700&family=Oswald:wght@400&display=swap">
<style>
:root{
  --ink:#222;
  --text:#555;
  --muted:#777;
  --dark:#333;
  --darker:#2a2a2a;
  --light-band:#efefef;
  --soft-band:#f5f3f3;
  --line:#dcdcdc;
  --accent:#2a8fd0;
  --white:#fff;
}
*{box-sizing:border-box;margin:0;padding:0}
html,body{width:1200px;height:2582px;overflow:hidden;background:var(--white)}
body{font-family:'Roboto',sans-serif;color:var(--text);position:relative}
.abs{position:absolute}
/* header */
.site-header{position:absolute;left:0;top:0;width:1200px;height:133px;background:var(--white)}
.brand{position:absolute;left:100px;top:38px;display:flex;align-items:center;gap:16px}
.brand-mark{width:58px;height:58px;border-radius:50%;background:#9a9a9a}
.brand-name{font-size:22px;font-weight:400;line-height:28px;color:var(--dark);text-transform:uppercase;width:130px}
.utility{position:absolute;right:97px;top:24px;font-size:11px;color:var(--muted);display:flex;gap:18px;align-items:center}
.utility svg{vertical-align:-2px;margin-right:5px}
.main-nav{position:absolute;left:537px;top:79px;display:flex;font-size:12px;font-weight:500;color:var(--ink)}
.main-nav a{display:block;height:35px;line-height:35px;padding:0 15px;margin-right:24px;color:var(--ink);text-decoration:none}
.main-nav a.active{background:var(--dark);color:var(--white);width:71px;text-align:center;padding:0}
.main-nav a:last-child{margin-right:0}
/* hero */
.hero{position:absolute;left:0;top:133px;width:1200px;height:559px;background:linear-gradient(180deg,#e9eaec 0%,#d6d8da 55%,#c9ccce 100%)}
.hero-photo{position:absolute;inset:0;background:radial-gradient(ellipse at 30% 40%,#cfc9c4 0%,transparent 55%),radial-gradient(ellipse at 75% 35%,#d8dadc 0%,transparent 60%)}
.hero-title{position:absolute;left:0;width:1200px;top:392px;text-align:center;font-family:'Oswald',sans-serif;font-size:58px;color:#4a4a4a;letter-spacing:-0.5px}
.hero-dots{position:absolute;left:548px;top:500px;display:flex;gap:26px}
.hero-dots span{width:16px;height:16px;border-radius:50%;background:#9a9a9a}
.hero-dots span.on{background:var(--accent)}
/* welcome */
.welcome{position:absolute;left:0;top:692px;width:1200px;height:179px;background:var(--light-band);text-align:center}
.welcome h1{margin-top:32px;font-size:26px;font-weight:300;color:var(--dark)}
.welcome p{width:952px;margin:14px auto 0;font-size:11.5px;line-height:19.5px;color:var(--muted)}
/* what we do */
.services{position:absolute;left:0;top:871px;width:1200px;height:446px;background:var(--white)}
.section-title{font-size:25px;font-weight:400;color:var(--ink);text-transform:uppercase}
.services-intro{position:absolute;left:100px;top:42px;width:466px}
.services-intro h3{margin-top:8px;font-size:16px;font-weight:400;color:var(--ink)}
.services-intro p{margin-top:14px;font-size:11.5px;line-height:20px;color:var(--muted)}
.btn-dark{display:block;background:var(--dark);color:var(--white);font-size:12px;font-weight:500;text-align:center;border-radius:3px;text-transform:uppercase}
.services-intro .btn-dark{position:absolute;top:304px;width:158px;height:48px;line-height:48px}
.service-grid{position:absolute;left:599px;top:41px;width:503px;height:348px;display:grid;grid-template-columns:1fr 1fr;grid-template-rows:1fr 1fr;border:1px solid var(--line)}
.service-card{border:1px solid var(--line);text-align:center;padding-top:18px;color:var(--ink)}
.service-card.featured{background:var(--dark);color:var(--white)}
.service-card h4{margin-top:8px;font-size:16px;font-weight:500;text-transform:uppercase}
.service-card p{width:200px;margin:6px auto 0;font-size:11px;line-height:17px}
/* our thinking */
.thinking{position:absolute;left:0;top:1317px;width:1200px;height:405px;background:var(--soft-band)}
.thinking-photo{position:absolute;left:100px;top:57px;width:497px;height:282px;border:6px solid var(--white);box-shadow:0 12px 16px rgba(0,0,0,.15);background:linear-gradient(135deg,#b9c4cf 0%,#7d9ac0 45%,#a9825f 60%,#9fb3cc 100%)}
.thinking-copy{position:absolute;left:640px;top:62px;width:462px}
.thinking-copy p{margin-top:16px;font-size:11.5px;line-height:20px;color:var(--muted);text-align:justify}
.thinking-copy .btn-dark{position:absolute;top:239px;width:112px;height:45px;line-height:45px}
/* feeds */
.feeds{position:absolute;left:0;top:1722px;width:1200px;height:595px}
.chirp-head{position:absolute;left:100px;top:50px}
.follow-btn{position:absolute;left:640px;top:50px;width:100px;height:34px;border:1px solid #9fc3de;border-radius:3px;background:linear-gradient(#fff,#e6eef5);font-size:15px;font-weight:700;color:#24588a;text-align:center;line-height:32px}
.chirp{position:absolute;left:100px;width:640px}
.chirp-thumb{position:absolute;left:0;top:0;width:134px;height:110px}
.chirp-body{position:absolute;left:163px;top:0;width:477px}
.meta{font-size:11px;color:var(--accent)}
.chirp-body h5{margin-top:6px;font-size:11.5px;font-weight:500;color:var(--ink);text-transform:uppercase}
.chirp-body p{margin-top:18px;font-size:11.5px;line-height:20px;color:var(--muted)}
.news-head{position:absolute;left:790px;top:50px}
.news-arrows{position:absolute;left:1068px;top:54px;display:flex;gap:12px}
.news-item{position:absolute;left:790px;width:312px;padding-bottom:0}
.news-item p{margin-top:8px;font-size:11.5px;line-height:20px;color:var(--muted)}
.news-rule{position:absolute;left:790px;width:312px;height:1px;background:var(--line)}
/* footer */
.site-footer{position:absolute;left:0;top:2317px;width:1200px;height:207px;background:var(--dark);color:var(--white)}
.foot-col{position:absolute;top:45px}
.foot-col h6{font-size:15px;font-weight:500;text-transform:uppercase}
.foot-col p{margin-top:12px;font-size:12px;line-height:20px}
.contact-line{display:flex;align-items:center;gap:14px;margin-top:8px;font-size:12px}
.contact-line.phone{font-size:17px}
.newsletter-form{display:flex;margin-top:16px}
.newsletter-form span{width:166px;height:38px;background:var(--white);color:var(--ink);font-size:11px;line-height:38px;padding-left:14px}
.newsletter-form b{width:78px;height:38px;background:var(--accent);font-size:15px;font-weight:400;line-height:38px;text-align:center}
.social{display:flex;gap:18px;margin-top:20px}
.social span{width:34px;height:34px;background:#e8e8e8;border-radius:2px}
.bottom-bar{position:absolute;left:0;top:2524px;width:1200px;height:58px;background:var(--darker);border-top:1px solid #444;color:#ddd;font-size:12px;line-height:58px;text-align:center}
.bottom-bar small{position:absolute;right:76px;font-size:10px}
</style>
</head>
<body>

<header class="site-header">
  <div class="brand"><span class="brand-mark"></span><span class="brand-name">Lantrovale Group</span></div>
  <div class="utility">
    <span><svg width="12" height="9" viewBox="0 0 12 9"><rect x=".5" y=".5" width="11" height="8" fill="#777"/><path d="M.5.5 6 5 11.5.5" stroke="#fff" fill="none"/></svg>info@lantrovale.co</span>
    <span><svg width="10" height="10" viewBox="0 0 10 10"><circle cx="5" cy="3" r="2.5" fill="#777"/><path d="M0 10a5 4 0 0 1 10 0z" fill="#777"/></svg>My Account</span>
    <span>|</span>
    <span><svg width="9" height="11" viewBox="0 0 9 11"><rect y="5" width="9" height="6" fill="#777"/><path d="M2 5V3a2.5 2.5 0 0 1 5 0v2" stroke="#777" fill="none" stroke-width="1.5"/></svg>Login</span>
  </div>
  <nav class="main-nav">
    <a class="active">HOME</a><a>ABOUT US</a><a>WHAT WE DO</a><a>OUR THINKING</a><a>CONTACT US</a>
  </nav>
</header>

<section class="hero">
  <div class="hero-photo" role="img" aria-label="Photo of business people working together at a bright office desk with pens and papers"></div>
  <h2 class="hero-title">CONSULTING COMPANY</h2>
  <div class="hero-dots"><span></span><span class="on"></span><span></span></div>
</section>

<section class="welcome">
  <h1>WELCOME TO LANTROVALE GROUP</h1>
  <p>Denouncing pleasure and praising pain was born and I will give you a complete account of the system, and expound the actual teachings of the great explorer of the truth, the master-builder of human happiness. No one rejects, dislikes, or avoids pleasure itself, because it is pleasure, but because those who do not know how to pursue pleasure rationally encounter consequences that are extremely painful. Nor again is there anyone who loves or pursues or desires to obtain pain of itself, because it is pain.</p>
</section>

<section class="services">
  <div class="services-intro">
    <h2 class="section-title">What we do</h2>
    <h3>LOREM IPSUM DOLOR SIT AMET, LIBERO</h3>
    <p>Perspiciatis unde omnis iste natus error sit voluptatem accusantium doloremque laudantium, totam rem aperiam, eaque ipsa quae ab illo inventore veritatis et quasi</p>
    <p>Architecto beatae vitae dicta sunt explicabo. Nemo enim ipsam voluptatem quia voluptas sit aspernatur aut odit aut fugit, sed quia consequuntur magni dolores eos qui ratione voluptatem sequi nesciunt. Neque porro quisquam est, qui dolorem ipsum quia dolor sit amet, consectetur, adipisci velit, sed quia non numquam eius modi tempora incidunt ut labore et dolore magnam aliquam quaerat voluptatem quis nostrum exercitationem ullam corporis suscipit laboriosam, nisi ut aliquid ex ea commodi consequatur? Quis autem vel eum iure reprehenderit qui in ea voluptate velit esse quam nihil.</p>
    <span class="btn-dark">See more services</span>
  </div>
  <div class="service-grid">
    <div class="service-card featured">
      <svg width="56" height="56" viewBox="0 0 56 56"><circle cx="28" cy="28" r="18" fill="none" stroke="#fff" stroke-width="7" stroke-dasharray="6 5"/><circle cx="28" cy="28" r="12" fill="none" stroke="#fff" stroke-width="4"/><circle cx="28" cy="28" r="5" fill="#fff"/></svg>
      <h4>Development</h4>
      <p>Nemo enim ipsam voluptatem quia voluptas sit aspernatur aut odit aut fugit, sed quia consequuntur.</p>
    </div>
    <div class="service-card">
      <svg width="56" height="56" viewBox="0 0 56 56"><path d="M10 14h36l-4 8H14z" fill="#333"/><rect x="12" y="20" width="32" height="28" fill="#333"/><circle cx="34" cy="38" r="8" fill="#fff"/><circle cx="34" cy="38" r="5" fill="#333"/></svg>
      <h4>Software</h4>
      <p>Nemo enim ipsam voluptatem quia voluptas sit aspernatur aut odit aut fugit, sed quia</p>
    </div>
    <div class="service-card">
      <svg width="56" height="56" viewBox="0 0 56 56"><path d="M21 16v-5h14v5" fill="none" stroke="#333" stroke-width="4"/><rect x="8" y="16" width="40" height="30" rx="3" fill="#333"/><rect x="8" y="28" width="40" height="2" fill="#fff"/></svg>
      <h4>Professional</h4>
      <p>Nemo enim ipsam voluptatem quia voluptas sit aspernatur aut odit aut fugit, sed quia</p>
    </div>
    <div class="service-card">
      <svg width="60" height="56" viewBox="0 0 60 56"><path d="M2 20l12-6 10 4 8-3 10 2 16-3 0 12-12 14-10 4-14-8-12-6z" fill="#333"/><path d="M22 30l8 6M26 26l8 6" stroke="#fff" stroke-width="2"/></svg>
      <h4>Consultancy</h4>
      <p>Nemo enim ipsam voluptatem quia voluptas sit aspernatur aut odit aut fugit, sed quia</p>
    </div>
  </div>
</section>

<section class="thinking">
  <div class="thinking-photo" role="img" aria-label="Photo of a team stacking their hands together in the middle of a circle"></div>
  <div class="thinking-copy">
    <h2 class="section-title">Our Thinking</h2>
    <p>From the moment you enter our stunning spa, our expert team will help you say goodbye to all the stresses and strains of modern life.</p>
    <p>Using a range of massage disciplines and techniques, we will reinvigorate your body – creating a healthier mind in the process. Whether you are a woman, a man or part of a couple, we have a range of services aimed at getting you ready for the challenges of daily life. We have a specially designed couples room for added privacy and seclusion.</p>
    <span class="btn-dark">Read more</span>
  </div>
</section>

<section class="feeds">
  <h2 class="section-title chirp-head">Chirplet</h2>
  <span class="follow-btn">Follow</span>

  <article class="chirp" style="top:122px">
    <div class="chirp-thumb" role="img" aria-label="Blue magazine cover with a heartbeat line" style="background:linear-gradient(180deg,#1d3f8a,#2a66c4)"></div>
    <div class="chirp-body">
      <div class="meta">Mon, 15-12-2016 at 13:00:00 GMT</div>
      <h5>Future proofing" your #analytics / #data science skills</h5>
      <p>Dear Valued Clients, Please be advised that CHF pairs will not be available for dummy text of the printing and typesetting industry. Lorem Ipsum has been the industry's standard dummy text ever since the.</p>
    </div>
  </article>
  <article class="chirp" style="top:274px">
    <div class="chirp-thumb" role="img" aria-label="Colourful seasonal sale banner" style="background:linear-gradient(135deg,#f2e6d9,#4aa6c8 50%,#e9d3c0)"></div>
    <div class="chirp-body">
      <div class="meta">Mon, 15-12-2016 at 13:00:00 GMT</div>
      <h5>The Marlowe Home #endofseasonsale</h5>
      <p>Dear Valued Clients, Please be advised that CHF pairs will not be available for dummy text of the printing and typesetting industry. Lorem Ipsum has been the industry's standard dummy text ever since the.</p>
    </div>
  </article>
  <article class="chirp" style="top:425px">
    <div class="chirp-thumb" role="img" aria-label="Amusement park with a ferris wheel under a blue sky" style="background:linear-gradient(180deg,#3d7fc4,#8fb9dd 60%,#9a7d6a)"></div>
    <div class="chirp-body">
      <div class="meta">Mon, 15-12-2016 at 13:00:00 GMT</div>
      <h5>Three times big #data made amusement parks better"</h5>
      <p>Dear Valued Clients, Please be advised that CHF pairs will not be available for dummy text of the printing and typesetting industry. Lorem Ipsum has been the industry's standard dummy text ever since the.</p>
    </div>
  </article>

  <h2 class="section-title news-head">Latest News</h2>
  <div class="news-arrows">
    <svg width="10" height="14" viewBox="0 0 10 14"><path d="M8 1 2 7l6 6" stroke="#999" fill="none" stroke-width="1.5"/></svg>
    <svg width="10" height="14" viewBox="0 0 10 14"><path d="M2 1l6 6-6 6" stroke="#999" fill="none" stroke-width="1.5"/></svg>
  </div>
  <div class="news-item" style="top:122px"><div class="meta">Agu14, 2016 at &nbsp; 13:00:00 GMT</div><p>Dear Valued Clients, Please be advised that CHF pairs will not be available for trading...</p></div>
  <div class="news-rule" style="top:207px"></div>
  <div class="news-item" style="top:241px"><div class="meta">Agu14, 2016 at &nbsp; 13:00:00 GMT</div><p>Dear Valued Clients, Please be advised that CHF pairs will not be available for trading...</p></div>
  <div class="news-rule" style="top:327px"></div>
  <div class="news-item" style="top:361px"><div class="meta">Agu14, 2016 at &nbsp; 13:00:00 GMT</div><p>Dear Valued Clients, Please be advised that CHF pairs will not be available for trading...</p></div>
  <div class="news-rule" style="top:446px"></div>
  <div class="news-item" style="top:480px"><div class="meta">Agu14, 2016 at &nbsp; 13:00:00 GMT</div><p>Dear Valued Clients, Please be advised that CHF pairs will not be available for trading...</p></div>
</section>

<footer class="site-footer">
  <div class="foot-col" style="left:98px;width:240px">
    <h6>Contact us</h6>
    <p>42 Linden Avenue 3rd Floor<br>Ashford, NY 10020, UK</p>
    <div class="contact-line phone"><svg width="18" height="18" viewBox="0 0 18 18"><path d="M4 1l3 4-2 2a10 10 0 0 0 6 6l2-2 4 3-2 3C8 17 1 10 1 3z" fill="none" stroke="#fff" stroke-width="1.3"/></svg>(+901) 555-0142</div>
    <div class="contact-line"><svg width="18" height="13" viewBox="0 0 18 13"><rect x=".5" y=".5" width="17" height="12" fill="none" stroke="#fff"/><path d="M.5.5 9 7l8.5-6.5" fill="none" stroke="#fff"/></svg>info@lantrovale.co</div>
  </div>
  <div class="foot-col" style="left:374px;width:230px">
    <h6>About us</h6>
    <p style="font-size:11.5px">Phasellus porta. Fusce susct varius mi. Cum sociis natoque penabus et magnis dis parturient montes, nascetur ridiculus mus. See more here http://ch.rp/K4Lqv2Tn</p>
  </div>
  <div class="foot-col" style="left:666px;width:250px">
    <h6>Newsletter</h6>
    <p style="font-size:11.5px">Excepteur sint occaecat cupidatat non proident, sunt in culpa qui officia deserunt mollit anim</p>
    <div class="newsletter-form"><span>Enter your email address</span><b>Sign Up</b></div>
  </div>
  <div class="foot-col" style="left:966px">
    <h6>Social media</h6>
    <div class="social"><span></span><span></span><span></span></div>
  </div>
</footer>
<div class="bottom-bar">2016 &nbsp;All Rights Reserved.<small>C 19</small></div>

</body>
</html>
```